Zeitloses Etiketten-Design für Zirbenlikör gesucht
Zielgruppe
Wir sind ein Betrieb der kunsthandwerkliche Gegenstände aus Holz herstellt, vor allem aus Zirbe. Da wir seit 3 Jahren auch Zirbenlikör herstellen, suchen wir für diese ein neues Etikett.
Aufgabenstellung
Zirbelikör wird aus den Zapfen der Zirbe hergestellt. Auf der Zirbe wachsen die Zapfen das erste mal nach ca. 20 Jahren. Sie wächst in ca. 1500 - 2500m Seehöhe und ist sehr wiederstandsfähig. Die Typische Farbe des Likörs ist Dunkelrot.
Ein paar dieser Dinge sollte man dem Etikett wieder finden. Vielleicht auch Berge im Hintergrund...
Klassisch, Zeitlos, Edel, vl. auch verspielt ( vor allem das Wort Zirbe), Wiedererkennungswert und meinen Namen: BRAUTIGL
Die Adresse kann gerne auch seitlich stehen.
Das alte Etikett habe ich selbst gemacht, es ist 6,5x10,5 cm. Fürs erste nicht so schlecht, zum expandieren eine Katastrophe.

```html
<!DOCTYPE html>
<html lang="de">
<head>
<meta charset="utf-8">
<title>Zirbe Likör – Etikett</title>
<link rel="stylesheet" href="https://fonts.googleapis.com/css2?family=Oswald:wght@300;400;500&family=Roboto+Slab:wght@700&display=swap">
<style>
  :root {
    --page: #efece7;
    --paper: #ffffff;
    --frame: #9a9a9a;
    --red: #d2232a;
    --red-soft: #f3c9cb;
    --ink: #3a3a3a;
    --forest-light: #d9d9d9;
    --forest-mid: #6f6f6f;
    --forest-dark: #1f1f1f;
    --on-dark: #f2f2f2;
  }
  * { margin: 0; padding: 0; box-sizing: border-box; }
  html, body { width: 900px; height: 1200px; overflow: hidden; background: var(--page); }
  .label {
    position: absolute; left: 130px; top: 90px; width: 640px; height: 1020px;
    background: var(--paper); overflow: hidden;
    box-shadow: 0 2px 10px rgba(0,0,0,.08);
  }
  .label__frame {
    position: absolute; inset: 18px; border: 2px solid var(--frame); z-index: 3; pointer-events: none;
  }
  .label__forest {
    position: absolute; left: 0; right: 0; top: 500px; bottom: 0; z-index: 1;
    background: linear-gradient(to bottom, var(--paper) 0%, var(--forest-light) 14%, var(--forest-mid) 40%, var(--forest-dark) 100%);
  }
  .label__content { position: absolute; inset: 0; z-index: 2; text-align: center; }
  .brand-mark {
    position: absolute; top: 62px; left: 0; right: 0;
    display: flex; justify-content: center; align-items: center; gap: 8px;
    font-family: "Oswald", sans-serif; font-weight: 400; font-size: 18px; letter-spacing: 3px; color: var(--ink);
  }
  .brand-mark__dot { width: 8px; height: 8px; border-radius: 50%; background: var(--ink); }
  .kicker {
    position: absolute; top: 122px; left: 0; right: 0;
    font-family: "Roboto Slab", serif; font-weight: 700; font-size: 28px; letter-spacing: 1px; color: var(--ink);
  }
  .product-script {
    position: absolute; top: 178px; left: 90px; width: 460px; height: 190px;
    background: radial-gradient(ellipse at center, var(--red-soft) 0%, rgba(243,201,203,.35) 60%, rgba(255,255,255,0) 100%);
  }
  .product-type {
    position: absolute; top: 372px; left: 0; right: 0;
    font-family: "Oswald", sans-serif; font-weight: 500; font-size: 96px; line-height: 1; letter-spacing: 4px; color: var(--red);
  }
  .producer {
    position: absolute; top: 720px; left: 0; right: 0;
    font-family: "Oswald", sans-serif; font-weight: 300; font-size: 23px; line-height: 1.45; color: var(--on-dark);
  }
  .specs {
    position: absolute; top: 858px; left: 0; right: 0;
    display: flex; justify-content: center; align-items: center; gap: 12px;
    font-family: "Oswald", sans-serif; font-weight: 300; font-size: 23px; color: var(--on-dark);
  }
  .specs__divider { width: 2px; height: 30px; background: var(--on-dark); }
</style>
</head>
<body>
  <div class="label">
    <div class="label__forest" role="img" aria-label="Schwarzweißfoto eines nebligen Zirbenwaldes"></div>
    <div class="label__frame"></div>
    <div class="label__content">
      <div class="brand-mark"><span class="brand-mark__dot"></span>BRAUTIGL</div>
      <div class="kicker">HAUSGEMACHTER</div>
      <div class="product-script" role="img" aria-label="Handgeschriebener Schriftzug „Zirbe“ in Rot"></div>
      <div class="product-type">LIKÖR</div>
      <div class="producer">
        THOMAS BRAUTIGL<br>
        LINDENHOF GASSE 14<br>
        3710 WALDKIRCHEN
      </div>
      <div class="specs">
        <span>ALC 29,7 % VOL</span>
        <span class="specs__divider"></span>
        <span>0,5L</span>
        <span class="specs__divider"></span>
        <span>L-170912</span>
      </div>
    </div>
  </div>
</body>
</html>
```